Keystead Homebuyers website creation

A slick professional landing page it needs to be a very engaging custom designed landing page.

It must have a lead generation tool/box similar to my competitors that will recognise the address when they start to enter the address or postcode.

My main competitors websites to use ideas from to build trust and look correct are: www.brindlecrestholdings.com quillmarshkeys.com

Target Market(s)

People looking to sell their house or property fast. We will buy their property

Industry/Entity Type

Real Estate

Coding

Coded - Design and coding required

Number of Pages Required

1 page

Requirements
Must have
• A lead generation tool that is similar to my competitors to gather their essential details. (please check www.quillmarshkeys.com or www.brindlecrestholdings.com to see what i want.

It also must have all the aspects my competitors has on their landing page. All companies in this industry have this on the landing page. These include: Logos to build trust. Ours can be The Harbinger Logo, the seen on TV logo, The Evening Quorum online logo. Also we need a step by step process map to show the customer how it works.

If the customer is about to leave the page it Must have flash ups that ask the customer to fill in 4 boxes. first name, surname, email, Phone number and address. Check out quillmarshkeys.com to see what i want.

must have a comparison table similar to my competitors. I can include this on the draft.

Must have my frequently asked questions for google SEO ( I will upload these to here to the winner to add this page at the end.

It must be a slick professional design that tells people they are dealing with a company they can trust who has the funds on hand to purchase hundreds of property.
Nice to have
• It must be a slick professional design that tells people they are dealing with a company they can trust who has the funds on hand to purchase hundreds of property.
Should not have
• Anything cheap or tacky looking.

```html
<!DOCTYPE html>
<html lang="en">
<head>
<meta charset="utf-8">
<title>Keystead Homebuyers — Sell your property fast</title>
<link href="https://fonts.googleapis.com/css2?family=Roboto:wght@300;400;500;700;900&display=swap" rel="stylesheet">
<style>
:root{
  --blue:#2a8fd6;
  --blue-dark:#1f7cc0;
  --ink:#1d1d22;
  --dark:#2d2c35;
  --black:#111114;
  --grey-text:#6b6b73;
  --light-grey:#ededf0;
  --line:#c9c9cf;
  --white:#ffffff;
  --green:#1fa05a;
}
*{box-sizing:border-box;margin:0;padding:0}
html,body{width:1200px;height:3900px;overflow:hidden}
body{font-family:'Roboto',sans-serif;color:var(--ink);background:var(--white);position:relative}
section,header,footer{position:absolute;left:0;width:1200px}
.abs{position:absolute}
.icon{stroke:var(--blue);fill:none;stroke-width:2}

/* top bar */
.topbar{top:0;height:43px;background:var(--black);color:var(--white);font-size:12px;font-weight:500}
.topbar .contact{left:65px;top:14px;display:flex;gap:28px}
.topbar .contact span{display:flex;align-items:center;gap:7px}
.topbar .social{left:908px;top:15px;display:flex;gap:7px}
.topbar .social i{width:12px;height:12px;background:var(--white);display:block;border-radius:2px}
.topbar .cta{left:991px;top:0;width:144px;height:43px;background:var(--blue);color:var(--white);font-size:14px;font-weight:500;display:flex;align-items:center;justify-content:center}

/* hero */
.hero{top:43px;height:494px;background:linear-gradient(#ffffff 0%,#f4f4f6 40%,#dcdde2 100%)}
.brand{display:flex;align-items:center;gap:6px;font-weight:400;color:var(--blue)}
.brand .mark{width:18px;height:18px;background:var(--blue);border-radius:3px}
.hero .brand{left:65px;top:30px;font-size:13px}
.nav{display:flex;gap:48px;font-size:14px;color:var(--ink)}
.hero .nav{right:65px;top:34px}
.nav .active{color:var(--blue)}
.city{left:0;top:280px;width:1200px;height:214px;background:linear-gradient(180deg,rgba(120,122,132,0) 0%,#8d8f98 35%,#4a4b53 75%,#2e2e34 100%)}
.hero h1{left:0;width:1200px;top:115px;text-align:center;font-size:50px;font-weight:500;letter-spacing:-.3px}
.search{left:203px;width:797px;height:56px;border-bottom:2px solid var(--blue)}
.search .ph{position:absolute;left:12px;top:14px;font-size:26px;font-weight:300;color:#333}
.search .btn{position:absolute;right:0;top:8px;width:142px;height:42px;background:var(--blue);color:var(--white);font-size:14px;font-weight:700;display:flex;align-items:center;justify-content:center}
.hero .search{top:222px}
.hero .tag{left:0;width:1200px;top:304px;text-align:center;font-size:19px}

/* process band */
.process{top:537px;height:194px;background:var(--dark);color:var(--white)}
.process .eyebrow{left:65px;top:42px;font-size:14px;font-weight:700}
.process h2{left:65px;top:66px;font-size:29px;font-weight:500;color:var(--blue)}
.process .lead{left:65px;top:110px;width:380px;font-size:14px;line-height:20px;color:#cfcfd6}
.step{width:185px}
.step .head{display:flex;gap:10px;align-items:flex-start;color:var(--blue);font-size:15px;line-height:18px}
.step p{margin-top:16px;font-size:11px;line-height:16px;color:#cfcfd6}

/* about */
.about{top:731px;height:411px}
.about .logo-big{left:65px;top:220px;width:400px;text-align:center;font-size:34px;color:var(--ink)}
.about .logo-big b{color:var(--blue);font-weight:400}
.about .logo-big .mark{width:40px;height:40px;background:var(--blue);border-radius:6px;margin:0 auto 22px}
.about h2{left:500px;top:47px;width:540px;font-size:24px;font-weight:400;line-height:28px}
.about .body{left:500px;top:148px;width:620px;font-size:14px;line-height:21px;color:var(--grey-text)}
.about .punch{left:500px;top:225px;font-size:23px}
.about .punch span{color:var(--blue)}
.about .rule{left:500px;top:272px;width:615px;height:1px;background:var(--line)}
.feature{display:flex;gap:12px;align-items:center;font-size:14px;line-height:18px}

/* video */
.video{top:1142px;height:419px}
.slide-side{top:21px;height:377px;background:linear-gradient(120deg,#5a4238,#8f6a55 50%,#3a3330)}
.slide-main{left:188px;top:0;width:823px;height:419px;background:linear-gradient(180deg,#dcd6d0 0%,#b98d70 45%,#7d5a3e 75%,#5f8f2d 100%);box-shadow:0 10px 30px rgba(0,0,0,.25)}
.play{left:562px;top:172px}

/* cta */
.cta-box{top:1631px;left:65px;width:1070px;height:351px;background:linear-gradient(135deg,#2d92da,#237fc4);box-shadow:0 10px 24px rgba(0,0,0,.18)}
.cta-box h2{left:0;width:1070px;top:60px;text-align:center;color:var(--white);font-size:49px;font-weight:700}
.cta-box .sub{left:0;width:1070px;top:136px;text-align:center;color:var(--white);font-size:22px;font-weight:500}
.cta-box .search{left:138px;top:210px;border-bottom-color:var(--white)}
.cta-box .search .ph{color:var(--white)}
.cta-box .search .btn{background:var(--blue-dark)}

/* steps */
.how{top:2043px;height:547px}
.eyebrow-c{left:0;width:1200px;text-align:center;font-size:13px;font-weight:700}
.title-c{left:0;width:1200px;text-align:center;font-size:28px;font-weight:500;color:var(--blue)}
.sub-c{left:0;width:1200px;text-align:center;font-size:14px;color:var(--grey-text)}
.ring{width:212px;height:212px;border-radius:50%;background:#ececef;box-shadow:0 6px 16px rgba(0,0,0,.08)}
.ring .photo{position:absolute;left:16px;top:16px;width:180px;height:180px;border-radius:50%}
.ring .num{position:absolute;left:144px;top:8px;width:58px;height:58px;border-radius:50%;background:var(--blue);border:4px solid var(--white);color:var(--white);font-size:16px;font-weight:500;display:flex;align-items:center;justify-content:center}
.connector{height:2px;background:#b9d7ee;top:248px}
.step-text{width:260px;text-align:center}
.step-text h3{font-size:19px;font-weight:500}
.step-text p{margin-top:10px;font-size:14px;line-height:21px;color:var(--grey-text)}

/* reviews */
.reviews{top:2590px;height:509px;background:var(--light-grey)}
.review{width:320px;text-align:center}
.avatar{width:72px;height:72px;border-radius:50%;margin:0 auto;background:linear-gradient(#bdb6b0,#6d625b);border:2px solid var(--white);box-shadow:0 0 0 1px #999}
.review h3{margin-top:14px;font-size:19px;font-weight:500}
.review p{margin-top:8px;font-size:14px;line-height:21px;color:var(--grey-text)}
.stars{display:flex;gap:4px}
.stars i{width:31px;height:31px;background:var(--green);display:block}

/* press */
.press{top:3099px;height:151px;display:flex;align-items:center;justify-content:space-between;padding:0 65px}
.press span{font-size:19px;font-weight:900;color:#222}
.press .light{font-weight:400;font-size:15px}
.press i{display:block;background:#c9d6e6;border-radius:4px}

/* contact */
.contact-sec{top:3250px;height:540px}
.form-side{left:0;top:0;width:749px;height:540px;background:var(--blue);color:var(--white)}
.form-side h2{left:65px;top:68px;font-size:27px;font-weight:500}
.field{height:48px;border-bottom:1.5px solid rgba(255,255,255,.85);font-size:19px;font-weight:300;padding:8px 0 0 14px}
.form-side .btn{left:67px;top:426px;width:141px;height:42px;background:var(--dark);color:var(--white);font-size:14px;font-weight:700;display:flex;align-items:center;justify-content:center}
.info-side{left:749px;top:0;width:451px;height:540px;background:var(--dark);color:var(--white)}
.info-side h2{left:30px;top:68px;font-size:27px;font-weight:500}
.info{left:28px;display:flex;gap:30px}
.info .txt{font-size:19px;line-height:25px}
.info .txt b{font-weight:700}
.info-side .social{left:30px;top:455px;display:flex;gap:12px}
.info-side .social i{display:block;width:24px;height:24px;background:var(--white);border-radius:3px}

/* footer */
.footer{top:3790px;height:110px;background:var(--white)}
.footer .brand{left:65px;top:42px;font-size:20px}
.footer .copy{left:377px;top:47px;font-size:14px;color:var(--grey-text)}
.footer .nav{right:65px;top:47px}
</style>
</head>
<body>

<header class="topbar">
  <div class="abs contact">
    <span><svg width="11" height="11" viewBox="0 0 12 12"><path d="M2 1h3l1 3-2 1a7 7 0 0 0 3 3l1-2 3 1v3c-6 0-10-4-10-10z" fill="#2a8fd6"/></svg>0208 555 0142</span>
    <span><svg width="13" height="10" viewBox="0 0 13 10"><rect x=".5" y=".5" width="12" height="9" fill="#2a8fd6"/><path d="M.5.5l6 5 6-5" stroke="#111" fill="none"/></svg>hello@keysteadhomebuyers.com</span>
  </div>
  <div class="abs social"><i></i><i></i><i></i></div>
  <div class="abs cta">Get a cash offer</div>
</header>

<section class="hero">
  <div class="abs brand"><span class="mark"></span>Keystead Homebuyers</div>
  <nav class="abs nav"><span class="active">Home</span><span>How it Works</span><span>About us</span><span>Find Properties</span><span>Contact us</span></nav>
  <div class="abs city" role="img" aria-label="Monochrome city skyline photograph"></div>
  <h1 class="abs">Start with a free cash offer...</h1>
  <div class="abs search"><span class="ph">Start typing an address/passcode</span><span class="btn">Get a cash offer</span></div>
  <p class="abs tag">We will buy any type of property fast</p>
</section>

<section class="process">
  <p class="abs eyebrow">Our Process</p>
  <h2 class="abs">The process is simple...</h2>
  <p class="abs lead">We buy property quickly, regardless of the condition — and you won't pay solicitor or estate agent fees.</p>
  <div class="abs step" style="left:515px;top:40px">
    <div class="head"><svg width="36" height="44" viewBox="0 0 36 44" class="icon"><rect x="2" y="2" width="32" height="40" rx="2"/><rect x="7" y="10" width="7" height="6"/><rect x="7" y="22" width="7" height="6"/><path d="M18 13h11M18 25h11M7 35h22"/></svg><span>Fill in Online<br>Form</span></div>
    <p>Call us on 0203 555 0187 or fill in your details online through our Valuation Form.</p>
  </div>
  <div class="abs step" style="left:747px;top:40px">
    <div class="head"><svg width="40" height="40" viewBox="0 0 40 40" class="icon"><circle cx="20" cy="20" r="18"/><path d="M25 13c-2-2-10-2-10 3s10 3 10 8-8 5-11 2M20 9v22"/></svg><span>Receive<br>offer</span></div>
    <p>Once we've received the details of your property, we will make you an offer within 24 hours.</p>
  </div>
  <div class="abs step" style="left:966px;top:40px">
    <div class="head"><svg width="44" height="44" viewBox="0 0 44 44" class="icon"><path d="M4 2v40M4 6h36M10 6v4M34 6v4"/><rect x="8" y="10" width="32" height="14"/><path d="M12 17h6M22 17h14"/></svg><span>Sale<br>Agreed</span></div>
    <p>The sale will be agreed! Sit back, relax, and let us take care of all the work.</p>
  </div>
</section>

<section class="about">
  <div class="abs logo-big"><div class="mark"></div>Keystead <b>Homebuyers</b></div>
  <h2 class="abs">We'll buy any type of property, regardless of the condition — and you won't pay solicitor or estate agent fees.</h2>
  <p class="abs body">Selling your property has never been easier or quicker. Our friendly, professional and down-to-earth home buying service puts you in charge and takes away all the hassle, costs and uncertainty that come with selling in more traditional ways.</p>
  <p class="abs punch">Selling your property to us is <span>simple, fast, and hassle-free!</span></p>
  <div class="abs rule"></div>
  <div class="abs feature" style="left:500px;top:296px"><svg width="36" height="44" viewBox="0 0 36 44" class="icon"><rect x="2" y="2" width="32" height="40" rx="2"/><rect x="7" y="10" width="7" height="6"/><rect x="7" y="22" width="7" height="6"/><path d="M18 13h11M18 25h11M7 35h22"/></svg><span>No Estate<br>Agent Fees</span></div>
  <div class="abs feature" style="left:708px;top:296px"><svg width="36" height="44" viewBox="0 0 36 44" class="icon"><rect x="2" y="2" width="32" height="40" rx="2"/><rect x="7" y="10" width="7" height="6"/><rect x="7" y="22" width="7" height="6"/><path d="M18 13h11M18 25h11M7 35h22"/></svg><span>Any Location,<br>Any Condition!</span></div>
  <div class="abs feature" style="left:925px;top:296px"><svg width="36" height="44" viewBox="0 0 36 44" class="icon"><rect x="2" y="2" width="32" height="40" rx="2"/><rect x="7" y="10" width="7" height="6"/><rect x="7" y="22" width="7" height="6"/><path d="M18 13h11M18 25h11M7 35h22"/></svg><span>Completion as Quick<br>as 7 days</span></div>
</section>

<section class="video">
  <div class="abs slide-side" style="left:0;width:143px" role="img" aria-label="Previous slide: hands photograph"></div>
  <div class="abs slide-side" style="left:1055px;width:145px" role="img" aria-label="Next slide: hands photograph"></div>
  <div class="abs slide-main" role="img" aria-label="Video still: cupped hands holding a small model house on grass"></div>
  <svg class="abs play" width="76" height="76" viewBox="0 0 76 76"><circle cx="38" cy="38" r="36" fill="rgba(20,20,24,.75)"/><path d="M30 24l24 14-24 14z" fill="#fff"/></svg>
</section>

<section class="cta-box">
  <h2 class="abs">Get a free cash offer today!</h2>
  <p class="abs sub">We buy property directly and you won't pay any agent's fees</p>
  <div class="abs search"><span class="ph">Start typing an address/passcode</span><span class="btn">Get a cash offer</span></div>
</section>

<section class="how">
  <p class="abs eyebrow-c" style="top:13px">How It Works</p>
  <h2 class="abs title-c" style="top:36px">Follow Easy Steps</h2>
  <p class="abs sub-c" style="top:78px">We'll take the headache out of selling your property – with a quick and simple process</p>
  <div class="abs connector" style="left:357px;width:118px"></div>
  <div class="abs connector" style="left:721px;width:117px"></div>
  <div class="abs ring" style="left:132px;top:143px"><div class="photo" role="img" aria-label="Hands holding a model house over banknotes" style="background:linear-gradient(160deg,#d9e3ee,#c0392b 50%,#8a5a3c)"></div><span class="num">01</span></div>
  <div class="abs ring" style="left:492px;top:143px"><div class="photo" role="img" aria-label="Model house on stacks of coins" style="background:linear-gradient(160deg,#bcd3ea,#e0a33a 50%,#9c6a3a)"></div><span class="num">02</span></div>
  <div class="abs ring" style="left:855px;top:143px"><div class="photo" role="img" aria-label="Handshake over a model house and contract" style="background:linear-gradient(160deg,#f2f2f2,#d8c2ae 55%,#a98468)"></div><span class="num">02</span></div>
  <div class="abs step-text" style="left:112px;top:365px"><h3>Instant offer</h3><p>Get in touch and enter your<br>details to request an<br>instant offer</p></div>
  <div class="abs step-text" style="left:472px;top:365px"><h3>Property value</h3><p>We'll make you a cash offer<br>– which you can take or<br>leave, no pressure</p></div>
  <div class="abs step-text" style="left:835px;top:365px"><h3>Timetable</h3><p>You choose a moving date<br>which suits you – we'll<br>take care of the rest</p></div>
</section>

<section class="reviews">
  <p class="abs eyebrow-c" style="top:58px">Reviews</p>
  <h2 class="abs title-c" style="top:82px">Happy cutomers</h2>
  <div class="abs review" style="left:76px;top:160px"><div class="avatar" role="img" aria-label="Customer portrait"></div><h3>Owen Hartley</h3><p>I had a brilliant experience with Keystead<br>and would happily cross paths with them<br>again in the future. Lovely people who go out<br>their way to help you in any way they can.</p></div>
  <div class="abs review" style="left:440px;top:160px"><div class="avatar" role="img" aria-label="Customer portrait"></div><h3>Priya Lennox</h3><p>I had a brilliant experience with Keystead<br>and would happily cross paths with them<br>again in the future. Lovely people who go out<br>their way to help you in any way they can.</p></div>
  <div class="abs review" style="left:804px;top:160px"><div class="avatar" role="img" aria-label="Customer portrait"></div><h3>Maren Doyle</h3><p>I had a brilliant experience with Keystead<br>and would happily cross paths with them<br>again in the future. Lovely people who go out<br>their way to help you in any way they can.</p></div>
  <p class="abs sub-c" style="top:405px;color:var(--ink);font-size:15px">Our customers love us</p>
  <div class="abs stars" style="left:513px;top:430px"><i></i><i></i><i></i><i></i><i></i></div>
</section>

<section class="press">
  <span>Daily Lantern</span>
  <span>Cityline</span>
  <span class="light" style="font-weight:700">Streamcast</span>
  <span style="font-size:17px">Ledgerpoint</span>
  <span class="light" style="font-size:18px">The Evening Quorum online</span>
  <span class="light" style="font-weight:700">The Harbinger</span>
  <i style="width:26px;height:26px"></i>
  <i style="width:70px;height:22px;background:#1f3f7a"></i>
  <i style="width:22px;height:22px;border-radius:50%;background:#b48a3a"></i>
  <i style="width:36px;height:26px"></i>
  <i style="width:30px;height:26px;background:#e0c3d8"></i>
  <i style="width:80px;height:20px;background:#bcd6ee"></i>
</section>

<section class="contact-sec">
  <div class="abs form-side">
    <h2 class="abs">Receive a free cash offer...</h2>
    <div class="abs field" style="left:65px;top:128px;width:263px">Your Name:*</div>
    <div class="abs field" style="left:385px;top:128px;width:263px">Telephone:*</div>
    <div class="abs field" style="left:65px;top:202px;width:263px">Email:</div>
    <div class="abs field" style="left:385px;top:202px;width:263px">Property Type:*</div>
    <div class="abs field" style="left:65px;top:276px;width:263px">Postcode:*</div>
    <div class="abs field" style="left:65px;top:350px;width:583px">How quickly do you want to sell?</div>
    <div class="abs btn">Make an offer</div>
  </div>
  <div class="abs info-side">
    <h2 class="abs">Get In Touch!</h2>
    <div class="abs info" style="top:132px"><svg width="54" height="44" viewBox="0 0 54 44" class="icon" style="stroke-width:3"><rect x="2" y="2" width="50" height="40" rx="4"/><path d="M4 6l23 18 23-18"/></svg><div class="txt">Email<br><b>support@keysteadhomebuyers.com</b></div></div>
    <div class="abs info" style="top:232px"><svg width="54" height="54" viewBox="0 0 54 54" class="icon" style="stroke-width:3"><circle cx="27" cy="20" r="11"/><path d="M12 22a15 15 0 0 1 30 0M6 52c2-10 10-15 21-15s19 5 21 15M38 28l-8 4"/></svg><div class="txt">Talk to our Experts<br><b>(123) 555-0199</b></div></div>
    <div class="abs info" style="top:340px"><svg width="54" height="60" viewBox="0 0 54 60" class="icon" style="stroke-width:3"><path d="M27 58S5 36 5 22a22 22 0 0 1 44 0c0 14-22 36-22 36z"/><circle cx="27" cy="22" r="8"/></svg><div class="txt">Address<br><b>48 Calder Row, Millbrook,<br>MB4 7QT</b></div></div>
    <div class="abs social"><i></i><i></i><i></i></div>
  </div>
</section>

<footer class="footer">
  <div class="abs brand"><span class="mark"></span>Keystead Homebuyers</div>
  <p class="abs copy">© Copyright 2021</p>
  <nav class="abs nav"><span>Home</span><span>How it Works</span><span>About us</span><span>Find Properties</span><span>Contact us</span></nav>
</footer>

</body>
</html>
```